Pine Ridge Traders, LLC- Global Beverage Company with 100% Cold Chain Logistics

Hey All, My Name is Dale, I am a young business owner in a competitive export space, but my niche is that I am shipping all of my beer around the world, "100% Cold Chain". This model is more costly, but it protects the integrity of the beer itself and will give folks in foreign countries the best representation of what US Craft Beer has to offer.

I am not a branding guy and don't claim to be one, I am a salesperson first, and will be referring to all of you to create something great that will be memorable.

I am looking for a basic Business Card Design for my Craft Beer Export company. I sell US Craft Beer in several countries around the globe. Austrailia, China, Taiwan, Chile, France, New Zealand... to name a few.

I am looking for a sleek, modern, and fresh design. Quickly!

Thanks for your consideration!

Cheers,

Dale

Target Market(s)

International

Contact Information for Business Card

Dale Corwin
Founder- Roving Hops Guy
Dale@PineRidgeTraders.example
@RovingHopsGuy- Instagram only
www.Pineridgetraders.example
@PineRidgeTradersAU- Instagram Only

Font styles to use
Serif

Colors
0592cd
ffffff

Requirements
Must have
• Name-
• Title-
• Email-
• Social Media Handle-
• Company Website-
Nice to have
• Nice Logo/ Images on Card
Should not have
• Tacky Beer Images

```html
<!DOCTYPE html>
<html lang="en">
<head>
<meta charset="utf-8">
<title>Dale Corwin – Business Card</title>
<link rel="stylesheet" href="https://fonts.googleapis.com/css2?family=Noto+Serif:wght@700&family=Open+Sans:wght@400&display=swap">
<style>
  :root {
    --ink-white: #ffffff;
    --ink-soft: rgba(255, 255, 255, 0.86);
    --deep-night: #0f1d26;
    --deep-teal: #0c3a4c;
    --mid-teal: #0a5670;
    --brand-blue: #0592cd;
    --sky-blue: #6aa8d8;
    --canvas-w: 1200px;
    --canvas-h: 722px;
  }

  html, body {
    margin: 0;
    padding: 0;
    width: var(--canvas-w);
    height: var(--canvas-h);
    overflow: hidden;
    background: var(--deep-night);
  }

  .card {
    position: relative;
    width: var(--canvas-w);
    height: var(--canvas-h);
    overflow: hidden;
  }

  .card__backdrop {
    position: absolute;
    inset: 0;
    background:
      radial-gradient(ellipse 55% 60% at 88% 85%, rgba(106,168,216,0.85) 0%, rgba(5,146,205,0.35) 45%, rgba(5,146,205,0) 75%),
      radial-gradient(ellipse 60% 55% at 55% 30%, rgba(10,86,112,0.9) 0%, rgba(12,58,76,0.4) 60%, rgba(12,58,76,0) 85%),
      linear-gradient(135deg, var(--deep-teal) 0%, var(--deep-night) 30%, var(--deep-teal) 55%, var(--mid-teal) 75%, var(--brand-blue) 100%);
  }

  .card__divider {
    position: absolute;
    left: 134px;
    top: 195px;
    width: 2px;
    height: 315px;
    background: var(--ink-white);
  }

  .card__name {
    position: absolute;
    left: 176px;
    top: 246px;
    margin: 0;
    font-family: "Noto Serif", Georgia, serif;
    font-weight: 700;
    font-size: 124px;
    line-height: 1;
    letter-spacing: -1px;
    color: var(--ink-white);
    white-space: nowrap;
  }

  .card__title {
    position: absolute;
    left: 180px;
    top: 394px;
    margin: 0;
    font-family: "Open Sans", Arial, sans-serif;
    font-weight: 400;
    font-size: 30px;
    line-height: 1;
    color: var(--ink-white);
    white-space: nowrap;
  }

  .card__contacts {
    position: absolute;
    left: 180px;
    top: 448px;
    margin: 0;
    padding: 0;
    list-style: none;
    display: grid;
    grid-template-columns: 340px 300px;
    row-gap: 10px;
    font-family: "Open Sans", Arial, sans-serif;
    font-weight: 400;
    font-size: 18px;
    line-height: 22px;
    color: var(--ink-soft);
    white-space: nowrap;
  }
</style>
</head>
<body>
  <main class="card">
    <div class="card__backdrop" role="img" aria-label="Layered pattern of rounded diamond tiles in deep teal fading to bright blue"></div>
    <div class="card__divider"></div>
    <h1 class="card__name">Dale Corwin</h1>
    <p class="card__title">Founder - Roving Hops Guy</p>
    <ul class="card__contacts">
      <li class="card__email">Dale@PineRidgeTraders.example</li>
      <li class="card__handle">Instagram @RovingHopsGuy</li>
      <li class="card__website">www.Pineridgetraders.example</li>
      <li class="card__handle">Instagram @PineRidgeTradersAU</li>
    </ul>
  </main>
</body>
</html>
```